Internet of Things Word Template

We need a new MS word template for our high-tech, Internet of Things business that matches the enclosed template in terms of content (chapters and subsections), but that updates the style to match our new house style, that has a clear and simple style sheet, uses NUMBERED sections (style = 1.2.3.4.5), a clear TOC and that more closely matches our new website and some of the new documents enclosed. Website (www.varomtek-iot.example) and house style guide www.varomtek-iot.example/private/style-guide. We prefer a lighter style, needs to be professional and credible. Current template has become difficult to work with, so prefer someone starting from scratch. Cover design should be more Internet of Things related than just security-oriented, and can draw from graphics on our website.

Target Market(s)

Technical decision makers at companies that make Internet of Things devices or chip manufacturers who make the chips that go into many devices across industries like medical, automotive, smart buildings, smart cities, car dealerships, trucking, etc.

Font styles to use
Sans Serif

Colors
1763aa
ec1f27
f78f20

Requirements
Must have
• Close relationship to house style from website... but...
Lightly implemented. Not too heavy. Doesn't look too dark when printed in black and white.
Must be easy for the average person to customize for their needs. My colleagues are not Word experts.
Nice to have
• A nicely designed cover. That's the one place to really express our brand.
Should not have
• No over-use of icons or illustrations in the document itself.

```html
<!DOCTYPE html>
<html lang="en">
<head>
<meta charset="utf-8">
<title>Varomtek IoT – Document Template</title>
<link rel="stylesheet" href="https://fonts.googleapis.com/css2?family=Work+Sans:wght@300;400;500;700;800&display=swap">
<style>
  :root {
    --brand-blue: #1763aa;
    --brand-red: #ec1f27;
    --brand-orange: #f78f20;
    --blue-light: #d3e3f3;
    --blue-line: #8fb5dc;
    --ink: #2b2d3a;
    --ink-soft: #6e7180;
    --paper: #ffffff;
    --backdrop: #ffffff;
  }
  * { box-sizing: border-box; margin: 0; padding: 0; }
  html, body { width: 1200px; height: 1001px; overflow: hidden; background: var(--backdrop); }
  body { position: relative; font-family: "Work Sans", Arial, sans-serif; color: var(--ink); }

  .page {
    position: absolute; width: 314px; height: 443px; background: var(--paper);
    overflow: hidden; box-shadow: 0 0 0 0.5px #e3e3e8;
  }
  .page--cover { left: 66px; top: 38px; }
  .page--toc   { left: 443px; top: 38px; }
  .page--p3    { left: 820px; top: 38px; }
  .page--p4    { left: 66px; top: 517px; }
  .page--p5    { left: 443px; top: 517px; }
  .page--p6    { left: 820px; top: 517px; }

  /* cover */
  .cover-art { position: absolute; left: 0; top: 0; }
  .brand { position: absolute; left: 41px; top: 262px; display: flex; align-items: center; gap: 6px; color: var(--brand-blue); font-weight: 800; font-size: 20px; line-height: 21px; letter-spacing: -0.3px; }
  .brand-dot { width: 9px; height: 9px; border-radius: 50%; background: var(--brand-orange); }
  .cover-title { position: absolute; left: 38px; top: 321px; font-size: 18px; font-weight: 400; color: var(--brand-blue); letter-spacing: 0.8px; }
  .cover-subtitle { position: absolute; left: 38px; top: 345px; font-size: 11px; font-weight: 400; color: var(--ink-soft); letter-spacing: 1px; }
  .cover-date { position: absolute; left: 38px; top: 376px; font-size: 6.5px; color: var(--ink-soft); }
  .cover-band { position: absolute; left: 0; bottom: 0; width: 100%; height: 30px; display: flex; }
  .cover-band .main { flex: 1; background: var(--brand-blue); }
  .cover-band .accent { width: 60px; background: var(--brand-orange); }

  /* inner pages */
  .content { position: absolute; left: 38px; top: 39px; width: 238px; }
  .chapter-title {
    font-size: 13.8px; font-weight: 400; color: var(--brand-blue); letter-spacing: 0.4px;
    padding-bottom: 2px; border-bottom: 1px solid var(--brand-blue); margin-bottom: 6px; white-space: nowrap;
  }
  .num { color: var(--brand-orange); margin-right: 5px; }
  .para-title { font-size: 9.3px; font-weight: 400; color: var(--brand-blue); letter-spacing: 0.4px; margin: 7px 0 3px; }
  .sub-heading { font-size: 6.2px; font-weight: 400; color: var(--ink-soft); margin-top: 4px; line-height: 7px; }
  .body-text { font-size: 4.7px; line-height: 6.6px; text-align: justify; color: var(--ink); margin-bottom: 4px; }
  .body-text--intro { color: var(--ink-soft); letter-spacing: 0.35px; font-weight: 300; }

  .bullets, .numbers { font-size: 4.7px; line-height: 7.1px; margin: 5px 0 6px 20px; }
  .bullets { list-style: disc; }
  .numbers { list-style: decimal; }
  .bullets li::marker { color: var(--brand-orange); }
  .numbers li::marker { color: var(--brand-blue); }
  .bullets li, .numbers li { padding-left: 3px; }

  /* toc */
  .toc { list-style: none; font-size: 7.1px; letter-spacing: 0.3px; color: var(--brand-blue); }
  .toc li { display: flex; line-height: 9.3px; white-space: nowrap; }
  .toc .n { display: inline-block; min-width: 14px; color: var(--brand-orange); }
  .toc .lvl2 .n { min-width: 16px; }
  .toc .lvl3 .n { min-width: 20px; }
  .toc .fill { flex: 1; border-bottom: 0.7px dotted var(--blue-line); margin: 0 1px 2.4px; }
  .toc .lvl1 { margin-top: 6.3px; }
  .toc .lvl1:first-child { margin-top: 0; }
  .toc .lvl2 { padding-left: 8px; }
  .toc .lvl1 + .lvl2 { margin-top: 6.3px; }
  .toc .lvl3 { padding-left: 8px; color: var(--ink-soft); }

  /* table */
  .data-table { width: 239px; border-collapse: collapse; margin-top: 7px; }
  .data-table th { background: var(--brand-blue); height: 14px; }
  .data-table td { height: 13.4px; border: 0.6px solid var(--blue-line); }
  .data-table tbody tr:nth-child(odd) td { background: var(--blue-light); }

  /* footer */
  .footer { position: absolute; left: 38px; top: 417px; width: 238px; font-size: 4.6px; color: var(--ink); display: flex; }
  .footer .site { width: 72px; }
  .footer .rights { flex: 1; }
  .footer-band { position: absolute; left: 0; top: 432px; width: 100%; height: 10px; display: flex; }
  .footer-band .main { width: 237px; background: var(--brand-blue); }
  .footer-band .light { flex: 1; background: var(--blue-light); }
  .footer-band .accent { width: 8px; background: var(--brand-orange); }
</style>
</head>
<body>

<!-- Cover -->
<section class="page page--cover">
  <svg class="cover-art" width="314" height="250" viewBox="0 0 314 250" role="img" aria-label="Connected devices network illustration on a blue field">
    <defs>
      <linearGradient id="coverFill" x1="0" y1="0" x2="0" y2="1">
        <stop offset="0" stop-color="#4f8ccb"/>
        <stop offset="1" stop-color="#1763aa"/>
      </linearGradient>
    </defs>
    <path d="M77 0 H314 V204 L212 231 Q160 243 140 210 Q132 196 128 182 Z" fill="url(#coverFill)"/>
  </svg>
  <div class="brand"><span>VAROMTEK<br>IOT</span><span class="brand-dot"></span></div>
  <h1 class="cover-title">TITLE GOES HERE</h1>
  <p class="cover-subtitle">SUBTITLE GOES HERE</p>
  <p class="cover-date">June 16, 2021</p>
  <div class="cover-band"><span class="main"></span><span class="accent"></span></div>
</section>

<!-- Table of contents -->
<section class="page page--toc">
  <div class="content">
    <h2 class="chapter-title">TABLE OF CONTENTS</h2>
    <ol class="toc">
      <li class="lvl1"><span class="n">1</span>CHAPTER TITILE GOES HERE<span class="fill"></span>3</li>
      <li class="lvl2"><span class="n">1.1</span>PARAGRAPH TITLE GOES HERE<span class="fill"></span>3</li>
      <li class="lvl2"><span class="n">1.2</span>PARAGRAPH TITLE GOES HERE<span class="fill"></span>3</li>
      <li class="lvl1"><span class="n">2</span>CHAPTER TITILE GOES HERE<span class="fill"></span>4</li>
      <li class="lvl1"><span class="n">3</span>CHAPTER TITILE GOES HERE<span class="fill"></span>5</li>
      <li class="lvl2"><span class="n">3.1</span>PARAGRAPH TITLE GOES HERE<span class="fill"></span>5</li>
      <li class="lvl2"><span class="n">3.2</span>PARAGRAPH TITLE GOES HERE<span class="fill"></span>5</li>
      <li class="lvl1"><span class="n">4</span>CHAPTER TITILE GOES HERE<span class="fill"></span>6</li>
      <li class="lvl2"><span class="n">4.1</span>PARAGRAPH TITLE GOES HERE<span class="fill"></span>6</li>
      <li class="lvl3"><span class="n">4.1.1</span>Paragraph Sub Heading<span class="fill"></span>6</li>
      <li class="lvl3"><span class="n">4.1.2</span>Paragraph Sub Heading<span class="fill"></span>6</li>
      <li class="lvl3"><span class="n">4.1.3</span>Paragraph Sub Heading<span class="fill"></span>6</li>
      <li class="lvl3"><span class="n">4.1.4</span>Paragraph Sub Heading<span class="fill"></span>6</li>
      <li class="lvl2"><span class="n">4.2</span>PARAGRAPH TITLE GOES HERE<span class="fill"></span>6</li>
      <li class="lvl3"><span class="n">4.2.1</span>Paragraph Sub Heading<span class="fill"></span>6</li>
      <li class="lvl3"><span class="n">4.2.2</span>Paragraph Sub Heading<span class="fill"></span>6</li>
    </ol>
  </div>
  <footer class="footer"><span class="site">www.varomtek-iot.example</span><span class="rights">© Corvane SA / All right reserved</span><span>2</span></footer>
  <div class="footer-band"><span class="main"></span><span class="light"></span><span class="accent"></span></div>
</section>

<!-- Page 3 -->
<section class="page page--p3">
  <div class="content">
    <h2 class="chapter-title"><span class="num">1</span>CHAPTER TITILE GOES HERE</h2>
    <p class="body-text body-text--intro">Lorem ipsum dolor sit amet, consectetuer adipiscing elit. Maecenas porttitor congue massa. Fusce posuere, magna sed pulvinar ultricies, purus lectus malesuada libero, sit amet commodo magna eros quis urna. Nunc viverra imperdiet enim. Fusce est. Vivamus a tellus. Pellentesque habitant morbi tristique senectus et netus et malesuada fames ac turpis egestas. Proin pharetra nonummy pede.</p>
    <h3 class="para-title"><span class="num">1.1</span>PARAGRAPH TITLE GOES HERE</h3>
    <p class="body-text">Lorem ipsum dolor sit amet, consectetuer adipiscing elit. Maecenas porttitor congue massa. Fusce posuere, magna sed pulvinar ultricies, purus lectus malesuada libero, sit amet commodo magna eros quis urna. Nunc viverra imperdiet enim. Fusce est. Vivamus a tellus. Pellentesque habitant morbi tristique senectus et netus et malesuada fames ac turpis egestas. Proin pharetra nonummy pede.</p>
    <p class="body-text">Mauris et orci. Aenean nec lorem. In porttitor. Donec laoreet nonummy augue. Suspendisse dui purus, scelerisque at, vulputate vitae, pretium mattis, nunc. Mauris eget neque at sem venenatis eleifend. Ut nonummy. Fusce aliquet pede non pede.</p>
    <p class="body-text">Suspendisse dapibus lorem pellentesque magna. Integer nulla. Donec blandit feugiat ligula. Donec hendrerit, felis et imperdiet euismod, purus ipsum pretium metus, in lacinia nulla nisl eget sapien. Donec ut est in lectus consequat consequat. Etiam eget dui. Aliquam erat volutpat. Sed at lorem in nunc porta tristique.</p>
    <h3 class="para-title" style="margin-top:26px"><span class="num">1.2</span>PARAGRAPH TITLE GOES HERE</h3>
    <p class="body-text">Lorem ipsum dolor sit amet, consectetuer adipiscing elit. Maecenas porttitor congue massa. Fusce posuere, magna sed pulvinar ultricies, purus lectus malesuada libero, sit amet commodo magna eros quis urna. Nunc viverra imperdiet enim. Fusce est. Vivamus a tellus. Pellentesque habitant morbi tristique senectus et netus et malesuada fames ac turpis egestas. Proin pharetra nonummy pede. Mauris et orci. Aenean nec lorem. In porttitor. Donec laoreet nonummy augue. Suspendisse dui purus, scelerisque at, vulputate vitae, pretium mattis, nunc. Mauris eget neque at sem venenatis eleifend. Ut nonummy.</p>
  </div>
  <footer class="footer"><span class="site">www.varomtek-iot.example</span><span class="rights">© Corvane SA / All right reserved</span><span>3</span></footer>
  <div class="footer-band"><span class="main"></span><span class="light"></span><span class="accent"></span></div>
</section>

<!-- Page 4 -->
<section class="page page--p4">
  <div class="content">
    <h2 class="chapter-title"><span class="num">2</span>CHAPTER TITILE GOES HERE</h2>
    <table class="data-table">
      <thead><tr><th colspan="4"></th></tr></thead>
      <tbody>
        <tr><td></td><td></td><td></td><td></td></tr>
        <tr><td></td><td></td><td></td><td></td></tr>
        <tr><td></td><td></td><td></td><td></td></tr>
        <tr><td></td><td></td><td></td><td></td></tr>
        <tr><td></td><td></td><td></td><td></td></tr>
        <tr><td></td><td></td><td></td><td></td></tr>
        <tr><td></td><td></td><td></td><td></td></tr>
        <tr><td></td><td></td><td></td><td></td></tr>
        <tr><td></td><td></td><td></td><td></td></tr>
        <tr><td></td><td></td><td></td><td></td></tr>
        <tr><td></td><td></td><td></td><td></td></tr>
        <tr><td></td><td></td><td></td><td></td></tr>
        <tr><td></td><td></td><td></td><td></td></tr>
        <tr><td></td><td></td><td></td><td></td></tr>
      </tbody>
    </table>
  </div>
  <footer class="footer"><span class="site">www.varomtek-iot.example</span><span class="rights">© Corvane SA / All right reserved</span><span>4</span></footer>
  <div class="footer-band"><span class="main"></span><span class="light"></span><span class="accent"></span></div>
</section>

<!-- Page 5 -->
<section class="page page--p5">
  <div class="content">
    <h2 class="chapter-title"><span class="num">3</span>CHAPTER TITILE GOES HERE</h2>
    <h3 class="para-title"><span class="num">3.1</span>PARAGRAPH TITLE GOES HERE</h3>
    <p class="body-text">Lorem ipsum dolor sit amet, consectetuer adipiscing elit. Maecenas porttitor congue massa. Fusce posuere, magna sed pulvinar ultricies, purus lectus malesuada libero, sit amet commodo magna eros quis urna. Nunc viverra imperdiet enim. Fusce est.</p>
    <ul class="bullets">
      <li>List with Bullets &nbsp;List with Bullets &nbsp;List with Bullets</li>
      <li>List with Bullets &nbsp;List with Bullets &nbsp;List with Bullets</li>
      <li>List with Bullets &nbsp;List with Bullets &nbsp;List with Bullets</li>
      <li>List with Bullets &nbsp;List with Bullets &nbsp;List with Bullets</li>
      <li>List with Bullets &nbsp;List with Bullets &nbsp;List with Bullets</li>
      <li>List with Bullets &nbsp;List with Bullets &nbsp;List with Bullets</li>
    </ul>
    <h3 class="para-title" style="margin-top:10px"><span class="num">3.2</span>PARAGRAPH TITLE GOES HERE</h3>
    <p class="body-text">Lorem ipsum dolor sit amet, consectetuer adipiscing elit. Maecenas porttitor congue massa. Fusce posuere, magna sed pulvinar ultricies, purus lectus malesuada libero, sit amet commodo magna eros quis urna. Nunc viverra imperdiet enim. Fusce est.</p>
    <ol class="numbers">
      <li>List with Numbers &nbsp;List with Numbers</li>
      <li>List with Numbers &nbsp;List with Numbers</li>
      <li>List with Numbers &nbsp;List with Numbers</li>
      <li>List with Numbers &nbsp;List with Numbers</li>
      <li>List with Numbers &nbsp;List with Numbers</li>
    </ol>
  </div>
  <footer class="footer"><span class="site">www.varomtek-iot.example</span><span class="rights">© Corvane SA / All right reserved</span><span>5</span></footer>
  <div class="footer-band"><span class="main"></span><span class="light"></span><span class="accent"></span></div>
</section>

<!-- Page 6 -->
<section class="page page--p6">
  <div class="content">
    <h2 class="chapter-title"><span class="num">4</span>CHAPTER TITILE GOES HERE</h2>
    <h3 class="para-title"><span class="num">4.1</span>PARAGRAPH TITLE GOES HERE</h3>
    <h4 class="sub-heading"><span class="num">4.1.1</span>Paragraph Sub Heading</h4>
    <p class="body-text">Lorem ipsum dolor sit amet, consectetuer adipiscing elit. Maecenas porttitor congue massa. Fusce posuere, magna sed pulvinar ultricies, purus lectus malesuada libero, sit amet commodo magna eros quis urna. Nunc viverra imperdiet enim. Fusce est. Vivamus a tellus.</p>
    <p class="body-text">Pellentesque habitant morbi tristique senectus et netus et malesuada fames ac turpis egestas. Proin pharetra nonummy pede. Mauris et orci. Aenean nec lorem. In porttitor. Donec laoreet nonummy augue.</p>
    <h4 class="sub-heading"><span class="num">4.1.2</span>Paragraph Sub Heading</h4>
    <p class="body-text">Lorem ipsum dolor sit amet, consectetuer adipiscing elit. Maecenas porttitor congue massa.</p>
    <h4 class="sub-heading"><span class="num">4.1.3</span>Paragraph Sub Heading</h4>
    <p class="body-text">Lorem ipsum dolor sit amet, consectetuer adipiscing elit. Maecenas porttitor congue massa. Fusce posuere, magna sed pulvinar ultricies, purus lectus malesuada libero, sit amet commodo magna eros quis urna. Nunc viverra imperdiet enim. Fusce est. Vivamus a tellus. Pellentesque habitant morbi tristique senectus et netus et malesuada fames ac turpis egestas. Proin pharetra nonummy pede. Mauris et orci. Aenean nec lorem.</p>
    <h4 class="sub-heading"><span class="num">4.1.4</span>Paragraph Sub Heading</h4>
    <p class="body-text">Lorem ipsum dolor sit amet, consectetuer adipiscing elit. Maecenas porttitor congue massa. Fusce posuere, magna sed pulvinar ultricies, purus lectus malesuada libero, sit amet commodo magna eros quis urna. Nunc viverra imperdiet enim.</p>
    <h3 class="para-title"><span class="num">4.2</span>PARAGRAPH TITLE GOES HERE</h3>
    <h4 class="sub-heading"><span class="num">4.2.1</span>Paragraph Sub Heading</h4>
    <p class="body-text">Lorem ipsum dolor sit amet, consectetuer adipiscing elit. Maecenas porttitor congue massa. Fusce posuere, magna sed pulvinar ultricies, purus lectus malesuada libero, sit amet commodo magna eros quis urna. Nunc viverra imperdiet enim.</p>
    <h4 class="sub-heading"><span class="num">4.2.2</span>Paragraph Sub Heading</h4>
    <p class="body-text">Lorem ipsum dolor sit amet, consectetuer adipiscing elit. Maecenas porttitor congue massa. Fusce posuere, magna sed pulvinar ultricies, purus lectus malesuada libero, sit amet commodo magna eros quis urna. Nunc viverra imperdiet enim.</p>
  </div>
  <footer class="footer"><span class="site">www.varomtek-iot.example</span><span class="rights">© Corvane SA / All right reserved</span><span>6</span></footer>
  <div class="footer-band"><span class="main"></span><span class="light"></span><span class="accent"></span></div>
</section>

</body>
</html>
```